Brimlow Oakville Cabernet Sauvignon-Wine label design

We need a package design for an up market wine brand named, Brimlow. It will be a Cabernet Sauvignon from the Oakville AVA of Napa Valley. We are looking for a stylish modern label that will stand out on a retail shelf. We want the label to be attention grabbing and stylish while presenting an up market luxury brand.
Updates

Sick

Requirements
Must have
• Must have the words(in order of importance)
-Brimlow
-Cabernet Sauvignon
-Oakville
-Napa Valley
-2018

Must be designed for a traditional "Bordeaux" style bottle (Bottle specs in uploaded files)
Should not have
• Any images of grapes, vineyards, wine glasses or bottles

```html
<!DOCTYPE html>
<html lang="en">
<head>
<meta charset="utf-8">
<title>Brimlow Cabernet Sauvignon – Label</title>
<link rel="stylesheet" href="https://fonts.googleapis.com/css2?family=Roboto+Condensed:wght@700&family=Outfit:wght@500&display=swap">
<style>
  :root {
    --stage-top: #2c2d32;
    --stage-mid: #4a4b50;
    --label-paper: #f1f1f1;
    --label-texture: #e4e4e4;
    --brand-rust: #b65a2b;
    --ink: #1c1c1c;
    --taupe: #8a8077;
    --dot: #9a908a;
  }
  * { margin: 0; padding: 0; box-sizing: border-box; }
  html, body { width: 1200px; height: 2279px; overflow: hidden; }
  body { position: relative; background: var(--stage-top); }

  .backdrop {
    position: absolute; left: 0; top: 0; width: 1200px; height: 900px;
    background: radial-gradient(ellipse at 50% 40%, var(--stage-mid) 0%, var(--stage-top) 70%);
  }

  .label {
    position: absolute; left: 0; top: 900px; width: 1200px; height: 1226px;
  }
  .label-texture {
    position: absolute; inset: 0;
    background: radial-gradient(circle at 50% 50%, var(--label-paper) 0%, var(--label-texture) 100%);
  }

  .brand-name {
    position: absolute; left: 0; right: 0; top: 270px;
    text-align: center;
    font-family: "Roboto Condensed", sans-serif; font-weight: 700;
    font-size: 150px; line-height: 1; letter-spacing: 46px; padding-left: 46px;
    color: var(--brand-rust);
  }

  .varietal {
    position: absolute; left: 0; right: 0; top: 428px;
    display: flex; align-items: center; justify-content: center; gap: 22px;
    font-family: "Roboto Condensed", sans-serif; font-weight: 700;
    font-size: 58px; line-height: 1; color: var(--ink);
  }
  .varietal-dot { width: 30px; height: 30px; border-radius: 50%; background: var(--dot); }

  .origin {
    position: absolute; left: 0; right: 0; top: 795px;
    text-align: center;
    font-family: "Outfit", sans-serif; font-weight: 500;
    font-size: 86px; line-height: 100px; letter-spacing: -1px; color: var(--ink);
  }

  .foot-band {
    position: absolute; left: 0; top: 2126px; width: 1200px; height: 153px;
    background: var(--taupe);
  }
</style>
</head>
<body>
  <div class="backdrop"></div>

  <section class="label">
    <div class="label-texture" role="img" aria-label="Fine grey crossed-line pattern across the white label paper"></div>
    <h1 class="brand-name">BRIMLOW</h1>
    <p class="varietal"><span class="varietal-dot"></span>CABERNET SAUVIGNON<span class="varietal-dot"></span></p>
    <p class="origin">Oakville<br>Napa Valley<br>2018</p>
  </section>

  <div class="foot-band"></div>
</body>
</html>
```